Tidal Sparks - Main Menu - Re-Design

I want to have a refresh for this app's main menu. There are some different items on the menu depending on the language (English vs. Non-English) and version (Pro vs. Free). I have attached screenshots of the different conditions. This app is a collection of brain training games.

Need designs for light and dark mode. Need designs for both portrait and landscape mode.

Here is a link to the app in Brisk Market.
https://apps.briskmarket.example/store/apps/details?id=tidalworks.tidalsparks

Here is a link to the app in the Orvel App Store.
https://depot.orvel.example/us/app/tidal-sparks-focus-drills/id519274063?ls=1&mt=8

```html
<!DOCTYPE html>
<html lang="en">
<head>
<meta charset="utf-8">
<title>Tidal Sparks – Main Menu Re-Design</title>
<link href="https://fonts.googleapis.com/css2?family=Roboto:ital,wght@0,300;0,400;0,500;0,700;0,900;1,300&display=swap" rel="stylesheet">
<style>
:root{
  --gold:#D4A71A;
  --brown:#4A3823;
  --pink:#DA5EC6;
  --cyan:#66D4FE;
  --peach:#F8BE9E;
  --white:#FFFFFF;
  --panel:#F4F4F8;
  --lavender:#E4E0F2;
  --bg-top:#D88DD9;
  --bg-bottom:#5A6BE6;
}
*{box-sizing:border-box;margin:0;padding:0}
html,body{width:1200px;height:628px;overflow:hidden}
body{font-family:'Roboto',sans-serif;background:linear-gradient(180deg,var(--bg-top),var(--bg-bottom));position:relative}
.screen{position:absolute;top:70px;width:226px;height:488px;border-radius:22px;overflow:hidden}

/* splash */
.splash{left:98px;background:linear-gradient(90deg,var(--pink) 50%,var(--cyan) 50%)}
.mascot{position:absolute;left:56px;top:136px;width:104px;height:90px;border-radius:48px 48px 40px 40px;background:radial-gradient(circle at 50% 40%,#FFA6D8,#F27CC4)}
.app-title{position:absolute;top:261px;width:100%;text-align:center;font-size:23px;font-weight:500;letter-spacing:-.3px;white-space:nowrap}
.app-title .w1{color:var(--cyan)}
.app-title .w2{color:var(--pink)}
.tagline{position:absolute;left:56px;top:293px;width:124px;height:45px;background:var(--peach);border-radius:12px;color:var(--white);font-style:italic;font-weight:300;font-size:12px;line-height:45px;text-align:center;white-space:nowrap}
.tagline-tail{position:absolute;left:138px;top:334px}
.pro-badge{position:absolute;left:73px;top:445px;width:80px;height:80px;border-radius:50%;background:var(--peach);color:var(--white);font-size:22px;text-align:center;padding-top:10px}

/* menu */
.menu{left:463px;background:var(--gold)}
.user-bar{position:absolute;left:9px;top:30px;display:flex;align-items:center;gap:6px;color:var(--white);font-size:13px}
.avatar{width:19px;height:19px;border-radius:50%;background:linear-gradient(135deg,#8B5A3C,#D9B48A)}
.settings{position:absolute;right:10px;top:31px}
.content{position:absolute;left:0;top:64px;width:100%;height:424px;background:var(--panel);border-radius:12px 12px 0 0}
.section-head{position:absolute;left:10px;width:205px;height:26px;background:var(--lavender);border-radius:10px 10px 0 0;display:flex;align-items:center;padding-left:8px;gap:6px}
.section-icon{width:16px;height:16px;border-radius:50%;background:#EDE3C6;border:1px solid #E2D2A0}
.section-title{font-size:10.5px;font-weight:700;color:var(--brown);letter-spacing:.3px;white-space:nowrap}
.view-all{position:absolute;right:8px;top:4px;width:48px;height:16px;border-radius:8px;background:var(--gold);color:var(--white);font-size:7px;text-align:center;line-height:16px}
.section-body{position:absolute;left:10px;width:205px;height:118px;background:var(--gold);border-radius:0 0 12px 12px}
.game{position:absolute;left:10px;width:185px;height:44px;background:var(--panel);border-radius:11px;display:flex;align-items:center;padding-left:10px;font-size:9px;color:var(--brown);white-space:nowrap}
.game-icon{width:20px;height:20px;border-radius:50%;background:#E7DDC4;margin-right:7px;display:flex;align-items:center;justify-content:center}
.game-icon span{width:9px;height:9px;background:var(--gold);border-radius:2px}
.score{position:absolute;right:29px;font-size:8.5px}
.go{position:absolute;right:10px}
.faded{opacity:.55}
.nav{position:absolute;left:0;bottom:0;width:100%;height:42px;background:var(--white);border-radius:12px 12px 0 0;display:flex;justify-content:space-around;align-items:flex-end;padding:0 8px 7px}
.nav-item{display:flex;flex-direction:column;align-items:center;gap:2px;font-size:6px;color:#222}
.nav-item.active{color:var(--gold)}

/* type & palette */
.divider{position:absolute;left:783px;top:107px;width:3px;height:200px;background:var(--brown)}
.specimen{position:absolute;left:808px;top:86px;font-size:148px;font-weight:900;color:var(--white);line-height:1;letter-spacing:8px}
.font-name{position:absolute;left:811px;top:250px;font-size:31px;font-weight:700;color:var(--white);letter-spacing:1px;white-space:nowrap}
.swatch{position:absolute;width:85px;height:85px;border-radius:20px}
</style>
</head>
<body>

<section class="screen splash">
  <div class="mascot" role="img" aria-label="Cheerful pink brain mascot illustration"></div>
  <h1 class="app-title"><span class="w1">Tidal</span> <span class="w2">Sparks</span></h1>
  <svg class="tagline-tail" width="30" height="20" viewBox="0 0 30 20"><path d="M0 0H28L22 16Z" fill="#F8BE9E"/></svg>
  <p class="tagline">“exercise your brain”</p>
  <div class="pro-badge">Pro</div>
</section>

<section class="screen menu">
  <div class="user-bar"><div class="avatar" role="img" aria-label="User profile photo"></div>Marla Quinlan</div>
  <svg class="settings" width="16" height="16" viewBox="0 0 16 16" fill="none" stroke="#fff" stroke-width="1.2"><circle cx="8" cy="8" r="6.5" stroke-dasharray="2.2 1.2"/><circle cx="8" cy="8" r="3"/></svg>
  <div class="content">
    <div class="section-head" style="top:13px"><span class="section-icon"></span><span class="section-title">Attention &amp; Focus</span><span class="view-all">View All</span></div>
    <div class="section-body" style="top:38px">
      <div class="game" style="top:11px"><span class="game-icon"><span></span></span>Attention training<span class="score">Score:--</span><svg class="go" width="13" height="13" viewBox="0 0 13 13" fill="none" stroke="#D4A71A"><circle cx="6.5" cy="6.5" r="5.8"/><path d="M5.5 4l2.5 2.5L5.5 9"/></svg></div>
      <div class="game" style="top:63px"><span class="game-icon"><span></span></span>Changing Focus<span class="score">Score:--</span><svg class="go" width="13" height="13" viewBox="0 0 13 13" fill="none" stroke="#D4A71A"><circle cx="6.5" cy="6.5" r="5.8"/><path d="M5.5 4l2.5 2.5L5.5 9"/></svg></div>
    </div>
    <div class="section-head" style="top:168px"><span class="section-icon"></span><span class="section-title">Mathematics</span><span class="view-all">View All</span></div>
    <div class="section-body" style="top:192px">
      <div class="game" style="top:11px"><span class="game-icon"><span></span></span>Math Operations<span class="score">Score:--</span><svg class="go" width="13" height="13" viewBox="0 0 13 13" fill="none" stroke="#D4A71A"><circle cx="6.5" cy="6.5" r="5.8"/><path d="M5.5 4l2.5 2.5L5.5 9"/></svg></div>
      <div class="game" style="top:64px"><span class="game-icon"><span></span></span>Math Flow<span class="score">Score:--</span><svg class="go" width="13" height="13" viewBox="0 0 13 13" fill="none" stroke="#D4A71A"><circle cx="6.5" cy="6.5" r="5.8"/><path d="M5.5 4l2.5 2.5L5.5 9"/></svg></div>
    </div>
    <div class="faded">
      <div class="section-head" style="top:320px"><span class="section-icon"></span><span class="section-title" style="font-weight:400">Memory</span><span class="view-all">View All</span></div>
      <div class="section-body" style="top:344px">
        <div class="game" style="top:11px"><span class="game-icon"><span></span></span>Memory Racer level 1<span class="score">Score:--</span><svg class="go" width="13" height="13" viewBox="0 0 13 13" fill="none" stroke="#D4A71A"><circle cx="6.5" cy="6.5" r="5.8"/><path d="M5.5 4l2.5 2.5L5.5 9"/></svg></div>
      </div>
    </div>
  </div>
  <nav class="nav">
    <div class="nav-item"><svg width="14" height="14" viewBox="0 0 14 14" fill="none" stroke="#222" stroke-width=".9"><rect x="1" y="1" width="12" height="12" rx="1"/><path d="M4 3v8M7 3v8M10 3v8"/></svg>Dashboard</div>
    <div class="nav-item active"><svg width="14" height="14" viewBox="0 0 14 14" fill="none" stroke="#D4A71A" stroke-width=".9"><rect x="1" y="5" width="12" height="7" rx="3.5"/><path d="M7 5V1"/><circle cx="4.5" cy="8.5" r="1"/><circle cx="9.5" cy="8.5" r="1"/></svg>Games</div>
    <div class="nav-item"><svg width="14" height="14" viewBox="0 0 14 14" fill="none" stroke="#222" stroke-width=".9"><rect x="1" y="2" width="12" height="11" rx="1"/><path d="M1 5h12M4 1v2M10 1v2"/></svg>Schedule</div>
    <div class="nav-item"><svg width="14" height="14" viewBox="0 0 14 14" fill="none" stroke="#222" stroke-width=".9"><path d="M3 13V9C1 7 1 3 5 1.5 9 0.5 13 3 12 7l1 2h-2v3H8v1"/></svg>Training</div>
    <div class="nav-item"><svg width="14" height="14" viewBox="0 0 14 14" fill="none" stroke="#222" stroke-width=".9"><path d="M1 5h12v8H1zM7 5v8"/><circle cx="7" cy="2.5" r="1.6"/></svg>learning</div>
  </nav>
</section>

<div class="divider"></div>
<div class="specimen">Aa</div>
<div class="font-name">Rovena Font Family</div>

<div class="swatch" style="left:811px;top:337px;background:var(--gold)"></div>
<div class="swatch" style="left:910px;top:337px;background:var(--brown)"></div>
<div class="swatch" style="left:811px;top:436px;background:var(--pink)"></div>
<div class="swatch" style="left:910px;top:436px;background:var(--cyan)"></div>
<div class="swatch" style="left:1010px;top:436px;background:var(--peach)"></div>

</body>
</html>
```